Bluestone Advisory & Mgmt - Professional Business Cards

Hi!

I am a Real Estate Developer and Construction Consultant.

I have a lot of inspiration from previous designs and would be open to using the attached Designs as a starting point. I would like to see these styles incorporated into your designs.

I really need professional business card to go with it that includes my important info.

Look forward to seeing your designs!.

Target Market(s)

My Target market are building owners, lawyers, consultants.

Industry/Entity Type

Real Estate Development

Contact Information for Business Card

My Name: Dorian Pelkey
My Title: Principle
Company Name: Bluestone Advisory & Mgmt, LLC
Address: 348 West 71st Street, 9th FL New York, NY 10010
Mobile: 917.806.3971
Website: bam-hvx.example

Font styles to use
Serif
Sans Serif

Colors

Designer to choose colors to be used in the design.

Requirements
Must have
• Must incorporate the logo attached or have new that looks similar.
• Must use professional font that will be seen and judged by wealthy land owners and developers.
• Must incorporate some of the color green.
Should not have
• Photo's or pictures of people or buildings of any kind.

```html
<!DOCTYPE html>
<html lang="en">
<head>
<meta charset="utf-8">
<title>Bluestone Advisory &amp; Mgmt, LLC – Business Card</title>
<link rel="stylesheet" href="https://fonts.googleapis.com/css2?family=Montserrat:wght@600;700&family=Open+Sans:wght@400;600&display=swap">
<style>
  :root {
    --page: #e9e6e1;
    --charcoal-dark: #242223;
    --charcoal-light: #3d3a3b;
    --band: #f1f1f1;
    --green: #4cba86;
    --green-light: #6fd3a3;
    --ink: #2b2b2b;
    --muted: #6b6b6b;
    --white: #ffffff;
  }
  * { box-sizing: border-box; margin: 0; padding: 0; }
  html, body { width: 1200px; height: 1023px; overflow: hidden; }
  body {
    background: var(--page);
    font-family: "Open Sans", Arial, sans-serif;
    position: relative;
  }
  .card {
    position: absolute;
    left: 190px;
    width: 820px;
    height: 469px;
    border-radius: 6px;
    overflow: hidden;
    box-shadow: 0 10px 28px rgba(0,0,0,.22);
  }

  /* Front */
  .card--front {
    top: 30px;
    background: linear-gradient(115deg, var(--charcoal-dark) 0%, var(--charcoal-light) 45%, var(--charcoal-dark) 100%);
  }
  .brand {
    position: absolute;
    left: 0; right: 0; top: 120px;
    display: flex;
    justify-content: center;
    align-items: center;
    gap: 22px;
  }
  .brand__dot {
    width: 18px; height: 18px;
    border-radius: 50%;
    background: var(--green-light);
  }
  .brand__rule {
    width: 1px; height: 72px;
    background: rgba(255,255,255,.55);
  }
  .brand__text { display: flex; flex-direction: column; gap: 6px; }
  .brand__name {
    font-family: "Montserrat", Arial, sans-serif;
    font-weight: 700;
    font-size: 40px;
    letter-spacing: 3px;
    color: var(--green-light);
  }
  .brand__tagline {
    font-family: "Montserrat", Arial, sans-serif;
    font-weight: 600;
    font-size: 17px;
    letter-spacing: 1px;
    color: #d9d9d9;
  }
  .web-band {
    position: absolute;
    left: 14px; right: 14px; bottom: 14px;
    height: 104px;
    background: var(--band);
    display: flex;
    align-items: center;
    padding-left: 230px;
    gap: 16px;
  }
  .web-band__url {
    font-family: "Open Sans", Arial, sans-serif;
    font-weight: 600;
    font-size: 20px;
    color: var(--ink);
    letter-spacing: .5px;
  }

  /* Back */
  .card--back {
    top: 524px;
    background: var(--white);
  }
  .back__stripe {
    position: absolute;
    left: 22px; top: 22px; bottom: 22px;
    width: 24px;
    background: var(--green);
  }
  .back__details {
    position: absolute;
    left: 80px; top: 60px;
    display: flex; flex-direction: column; gap: 8px;
    color: var(--ink);
    font-size: 17px;
  }
  .back__company {
    font-family: "Montserrat", Arial, sans-serif;
    font-weight: 700;
    font-size: 19px;
    margin-bottom: 6px;
  }
  .back__line { display: flex; align-items: center; gap: 10px; color: var(--muted); }
  .identity {
    position: absolute;
    right: 22px; bottom: 22px;
    width: 400px; height: 260px;
    background: linear-gradient(135deg, var(--green-light), var(--green));
    display: flex; flex-direction: column; justify-content: center;
    padding-left: 48px;
    color: var(--white);
  }
  .identity__name {
    font-family: "Montserrat", Arial, sans-serif;
    font-weight: 700;
    font-size: 36px;
    letter-spacing: 1px;
  }
  .identity__title {
    font-size: 17px;
    margin-top: 8px;
    opacity: .9;
  }
</style>
</head>
<body>
  <section class="card card--front" aria-label="Card front">
    <div class="brand">
      <span class="brand__dot"></span>
      <span class="brand__rule"></span>
      <div class="brand__text">
        <span class="brand__name">Bluestone</span>
        <span class="brand__tagline">Advisory &amp; Mgmt, LLC</span>
      </div>
    </div>
    <div class="web-band">
      <svg width="26" height="26" viewBox="0 0 24 24" fill="none" stroke="#2b2b2b" stroke-width="1.6" aria-hidden="true">
        <circle cx="12" cy="12" r="10"/>
        <ellipse cx="12" cy="12" rx="4.5" ry="10"/>
        <line x1="2" y1="12" x2="22" y2="12"/>
        <line x1="4" y1="7" x2="20" y2="7"/>
        <line x1="4" y1="17" x2="20" y2="17"/>
      </svg>
      <span class="web-band__url">www.bam-hvx.example</span>
    </div>
  </section>

  <section class="card card--back" aria-label="Card back">
    <div class="back__stripe"></div>
    <div class="back__details">
      <span class="back__company">Bluestone Advisory &amp; Mgmt, LLC</span>
      <span class="back__line">348 West 71st Street, 9th FL</span>
      <span class="back__line">New York, NY 10010</span>
      <span class="back__line">
        <svg width="16" height="16" viewBox="0 0 24 24" fill="#4cba86" aria-hidden="true">
          <path d="M6.6 10.8a15.1 15.1 0 0 0 6.6 6.6l2.2-2.2a1 1 0 0 1 1-.25 11.4 11.4 0 0 0 3.6.57 1 1 0 0 1 1 1V20a1 1 0 0 1-1 1A17 17 0 0 1 3 4a1 1 0 0 1 1-1h3.5a1 1 0 0 1 1 1c0 1.25.2 2.45.57 3.6a1 1 0 0 1-.25 1z"/>
        </svg>
        917.806.3971
      </span>
    </div>
    <div class="identity">
      <span class="identity__name">Dorian Pelkey</span>
      <span class="identity__title">Principle</span>
    </div>
  </section>
</body>
</html>
```